Website Design for a "Talent Recruitment Agency"

We are looking for a website design for the website of our "Talent Recruitment Agency"; which is called "Crestway Hub".
Our recruitment website "Crestway Hub" will be focusing on: "Crestway Hub: Linking People & Firms in Switzerland"; which means our target audience is two-folded:
(i) TALENT - that is currently residing in- or outside of Switzerland, and is open for and interested in the "Swiss Job Market".
(ii) COMPANIES - that are looking for talent for specific job vacancies in Switzerland.
With our "Crestway Hub" approach we inted to focus on Membership & Partnership:
(a)"Membership"(TALENT)
and
(b)"Partnership"(COMPANIES)
Some of the competitor sites we like are:
• www.plimora42.dk
• www.qelvo.ch
• www.brandolix.ch/en
A sitemap example of our website is attached.
Also attached is a "Crestway Hub" logo in .eps format and one in .jpeg format.
We very much look forward to receive your creative ideas.
Best regards,
Crestway Hub
Crestway Hub: Linking People & Firms in Switzerland.
Website: crestwayhub.ch - Twitter: CrestwayHubCH
Target Market(s)
(i) TALENT (with around 0-10 years of working experience), currently residing in- or outside of Switzerland, but eligible to work in Switzerland.
(ii) COMPANIES (national or international) that are based in Switzerland.
Industry/Entity Type
Recruitment

```html
<!DOCTYPE html>
<html lang="en">
<head>
<meta charset="utf-8">
<title>Crestway Hub – Linking People &amp; Firms in Switzerland</title>
<link href="https://fonts.googleapis.com/css2?family=Maven+Pro:wght@400;500&display=swap" rel="stylesheet">
<style>
  :root {
    --navy-top: #0c4670;
    --navy: #06304f;
    --navy-deep: #04253d;
    --orange: #f37021;
    --orange-btn: #fb7d2e;
    --blue: #0d7bc4;
    --blue-btn: #128ee0;
    --blue-text: #1d8fd8;
    --hero-bg: #e4e4e6;
    --ink: #111;
    --white: #fff;
    --brown: #6b2c08;
    --map-red: #990000;
  }
  * { margin: 0; padding: 0; box-sizing: border-box; }
  html, body { width: 1200px; height: 1169px; overflow: hidden; }
  body {
    position: relative;
    font-family: "Maven Pro", Arial, sans-serif;
    color: var(--white);
    background: linear-gradient(180deg, var(--navy-top) 0, var(--navy) 505px, var(--navy-deep) 506px, var(--navy-deep) 655px, var(--navy) 656px, var(--navy) 100%);
  }
  .abs { position: absolute; }

  /* header */
  .brand { left: 47px; top: 44px; display: flex; align-items: center; gap: 14px; }
  .brand-dot { width: 62px; height: 62px; border-radius: 50%; background: var(--orange); }
  .brand-name { font-size: 50px; font-weight: 500; color: var(--orange); line-height: 1; }
  .brand-tagline { left: 162px; top: 101px; font-size: 15px; color: var(--white); }

  .flags { left: 947px; top: 72px; display: flex; gap: 18px; }
  .flag { width: 19px; height: 12px; display: flex; }
  .flag i { flex: 1; display: block; }

  .nav { right: 84px; top: 99px; display: flex; gap: 24px; font-size: 13px; list-style: none; }
  .nav li.active { color: var(--orange); }

  /* hero */
  .hero { left: 47px; top: 167px; width: 1107px; height: 450px; background: var(--hero-bg); overflow: hidden; }
  .hero-photo { position: absolute; left: 0; top: 0; }
  .hero-copy { left: 438px; top: 78px; width: 720px; text-align: center; color: var(--ink); font-size: 27px; line-height: 34px; }
  .hero-copy .blue { color: var(--blue-text); }
  .hero-copy .orange { color: var(--orange); }
  .btn { width: 242px; height: 53px; line-height: 51px; text-align: center; font-size: 20px; color: var(--white); }
  .btn-talent { left: 678px; top: 212px; background: var(--blue-btn); border: 1px solid #0a6fb4; }
  .btn-company { left: 678px; top: 281px; background: var(--orange-btn); border: 1px solid #d55b12; }

  /* band */
  .band { left: 47px; top: 617px; width: 1107px; height: 151px; background: var(--blue); }
  .band-title { left: 48px; top: 14px; font-size: 34px; line-height: 42px; }
  .band-link { left: 48px; top: 108px; font-size: 20px; color: #b9d6ee; }
  .band-map { left: 856px; top: 10px; width: 200px; height: 114px; background: var(--map-red); border-radius: 40px 20px 50px 30px; }

  /* info columns */
  .info { left: 47px; top: 768px; width: 1107px; height: 305px; background: var(--orange); }
  .col { top: 40px; }
  .col h2 { font-size: 21px; font-weight: 400; margin-bottom: 16px; }
  .col p { font-size: 15.5px; line-height: 20px; }
  .col .entry { margin-bottom: 20px; }
  .col-about { left: 48px; width: 355px; }
  .col-jobs { left: 470px; width: 265px; }
  .col-events { left: 776px; width: 290px; }
  .more { top: 243px; font-size: 15px; font-style: italic; color: var(--brown); }
  .divider { top: 46px; height: 222px; border-left: 3px dotted var(--white); }

  /* footer */
  .copyright { left: 47px; top: 1089px; font-size: 13px; line-height: 18px; }
  .social { left: 777px; top: 1084px; display: flex; gap: 10px; }
  .social span { width: 37px; height: 38px; border-radius: 4px; display: block; }
  .footer-brand { left: 1009px; top: 1086px; display: flex; align-items: center; gap: 8px; }
  .footer-brand .dot { width: 30px; height: 30px; border-radius: 50%; background: var(--orange); }
  .footer-brand .name { font-size: 20px; font-weight: 500; color: var(--orange); }
</style>
</head>
<body>
  <header>
    <div class="abs brand"><span class="brand-dot"></span><span class="brand-name">Crestway Hub</span></div>
    <div class="abs brand-tagline">Crestway Hub: Linking People &amp; Firms in Switzerland</div>

    <div class="abs flags" aria-label="Languages">
      <span class="flag"><i style="background:#1f3f8f"></i><i style="background:#c8102e"></i><i style="background:#1f3f8f"></i></span>
      <span class="flag" style="flex-direction:column"><i style="background:#000"></i><i style="background:#d00"></i><i style="background:#fc0"></i></span>
      <span class="flag"><i style="background:#2a4ea0"></i><i style="background:#fff"></i><i style="background:#e0262e"></i></span>
      <span class="flag"><i style="background:#1a9f48"></i><i style="background:#fff"></i><i style="background:#d8262e"></i></span>
      <span class="flag" style="flex-direction:column"><i style="background:#c8102e"></i><i style="background:#fff"></i><i style="background:#21468b"></i></span>
    </div>

    <ul class="abs nav">
      <li class="active">Home</li><li>About</li><li>Talent</li><li>Companies</li><li>Jobs</li><li>Events</li><li>Contact</li>
    </ul>
  </header>

  <section class="abs hero">
    <svg class="hero-photo" width="1107" height="450" role="img" aria-label="Photo of three smiling business people meeting over coffee in a bright office">
      <polygon points="0,0 512,0 444,450 0,450" fill="#6b7482"/>
    </svg>
    <div class="abs hero-copy">
      Join our Network<br>to find your <span class="blue">desired career</span><br>or <span class="orange">the right talent</span> for your company
    </div>
    <div class="abs btn btn-talent">I’m a Talent</div>
    <div class="abs btn btn-company">We are Company</div>
  </section>

  <section class="abs band">
    <h1 class="abs band-title" style="font-weight:400">The right place to find talented professionals<br>or choosing a career in Switzerland</h1>
    <div class="abs band-link">Learn more &gt;&gt;</div>
    <div class="abs band-map" role="img" aria-label="Map of Switzerland"></div>
  </section>

  <section class="abs info">
    <div class="abs col col-about">
      <h2>ABOUT</h2>
      <p>Our recruitment website "Crestway Hub" will be focusing on: "Crestway Hub: Linking People &amp; Firms in Switzerland"; which means our target audience is two-folded: TALENT &amp; COMPANIES - that are looking for talent for specific job vacancies in Switzerland.</p>
    </div>
    <div class="abs more" style="left:48px">:: more details</div>
    <div class="abs divider" style="left:434px"></div>

    <div class="abs col col-jobs">
      <h2>JOBS</h2>
      <p class="entry">Trainees for Specialized Technical Trainee Program<br>09/04/2014</p>
      <p class="entry">Marketing Coordinator<br>28/03/2014</p>
    </div>
    <div class="abs more" style="left:470px">:: more available jobs</div>
    <div class="abs divider" style="left:748px"></div>

    <div class="abs col col-events">
      <h2>EVENTS</h2>
      <p class="entry">Return of the mega-merger as Larvenne and Holtrex turn cement into profits<br>09/04/2014</p>
      <p class="entry">Swiss startups get help with US market breakthrough<br>28/03/2014</p>
    </div>
    <div class="abs more" style="left:776px">:: more events</div>
  </section>

  <footer>
    <div class="abs copyright">Copyright 2014 crestwayhub.ch. All Rights Reserved.<br>Terms &amp; Conditions | Disclaimer</div>
    <div class="abs social" aria-label="Social links">
      <span style="background:#5bc3e6"></span>
      <span style="background:#3b5b9a"></span>
      <span style="background:#2c7fb8"></span>
      <span style="background:#c6dc2a"></span>
    </div>
    <div class="abs footer-brand"><span class="dot"></span><span class="name">Crestway Hub</span></div>
  </footer>
</body>
</html>
```